Brightwell Korrin Dental Practice Anniversary Flyer

Letter Box Drop Flyer (DL size)

We need a flyer design for letterbox drop. On the occasion of our practice anniversary in march 2014 we want to offer our patients special discounts.

1, vexa teeth whitening for 699$ (usually costs 1200$)
2. 10 percent discount on all Dental treatments like Orthavue, Pelbrook set, Crowns and Bridges, Mouthguards and Implants.

Attached Brightwell Korrin logo.

```html
<!DOCTYPE html>
<html lang="en">
<head>
<meta charset="utf-8">
<title>Brightwell Korrin Dental Practice – Special Anniversary Discounts</title>
<link href="https://fonts.googleapis.com/css2?family=Caveat:wght@500&family=Noto+Sans:wght@700&display=swap" rel="stylesheet">
<style>
  :root {
    --tone-top: #dcb8ab;
    --tone-mid: #cf9a93;
    --tone-bottom: #e2c4b6;
    --ink: #000000;
    --band: rgba(255, 255, 255, 0.45);
    --panel: #ffffff;
    --brand: #3f8a2e;
  }
  html, body {
    margin: 0;
    padding: 0;
    overflow: hidden;
    background: #ffffff;
  }
  .flyer {
    position: relative;
    width: 1200px;
    height: 566px;
    overflow: hidden;
  }
  .photo-area {
    position: absolute;
    inset: 0;
    background: linear-gradient(180deg, var(--tone-top) 0%, var(--tone-mid) 50%, var(--tone-bottom) 100%);
  }
  .title-band {
    position: absolute;
    left: 0;
    top: 40px;
    width: 1200px;
    height: 130px;
    background: var(--band);
  }
  .headline {
    position: absolute;
    left: 0;
    top: 38px;
    width: 1200px;
    margin: 0;
    text-align: center;
    font-family: "Caveat", cursive;
    font-weight: 500;
    font-size: 88px;
    line-height: 120px;
    letter-spacing: 2px;
    color: var(--ink);
  }
  .offers {
    position: absolute;
    left: 20px;
    top: 236px;
    margin: 0;
    padding: 0;
    list-style: none;
    font-family: "Noto Sans", sans-serif;
    font-weight: 700;
    font-size: 27px;
    line-height: 40px;
    letter-spacing: 0.4px;
    color: var(--ink);
  }
  .offers li { margin: 0 0 8px; }
  .offers li:last-child { margin: 0; }
  .brand-panel {
    position: absolute;
    left: 836px;
    top: 376px;
    width: 320px;
    height: 148px;
    background: var(--panel);
    display: flex;
    align-items: center;
    justify-content: center;
  }
  .brand-name {
    font-family: "Noto Sans", sans-serif;
    font-weight: 700;
    font-size: 32px;
    color: var(--brand);
  }
</style>
</head>
<body>
  <main class="flyer">
    <div class="photo-area" role="img" aria-label="Close-up photograph of a smiling mouth with white teeth"></div>
    <div class="title-band"></div>
    <h1 class="headline">Special Anniversary discounts</h1>
    <ul class="offers">
      <li>Vexa teeth whitening for 699$ (usually costs 1200$)</li>
      <li>10 percent discount on all Dental treatments like<br>Orthavue, Pelbrook set, Crowns and Bridges, Mouthguards and Implants.</li>
    </ul>
    <div class="brand-panel">
      <span class="brand-name">Brightwell Korrin</span>
    </div>
  </main>
</body>
</html>
```